'Orla Property Development' Business Card

Business Card Features:

High Quality (potentially textured) thick card - preference is white textured card

Logo (supplied)

We plan to use the vertical logo as the main logo. But i am happy for people to use either if they find it works better for the design of the card.

The building icon and also the insert to the 'E' is in a metallic finish, i think this should be finished in a metallic embossed or raised style.
Updates

Please note i have attached both a horizontal and Vertical Logo for your reference. We plan to use the vertical logo as the main logo. But i am happy for people to use either if they find it works better for the design of the card.

Please note i am considering having the cards made on stainless steel. This introduces the option of having cut outs in the card and etching or printing for the design. If you have a good concept for this please submit.

http://www.quorvantprint.co.uk/black-metal-cards# this is a site that makes the metal cards to offer some direction . . . . Please note i am basic the selection o the best design, if that means normal print cards on paper then this is what i will choose. But there are some great options with the metal. Thanks.

Industry/Entity Type

Building

Requirements
Must have
• Helvetica font to details side of card - logo as supplied to opposite side.

Card Details:

Darren Ashcombe
Managing Director

+61 438 615 207
+61 3 8276 4139

PO Box 73
Bentleigh, VIC 3024

darren@orla.properties

www.orla.properties

```html
<!DOCTYPE html>
<html lang="en">
<head>
<meta charset="utf-8">
<title>Orla Property Development – Business Card</title>
<link rel="stylesheet" href="https://fonts.googleapis.com/css2?family=Arimo:wght@400;700&display=swap">
<style>
  :root {
    --backdrop: #d8d3cb;
    --card-black: #0c0c0c;
    --card-sheen: #262626;
    --metal: #b9b9b9;
    --metal-dim: #8a8a8a;
    --text-light: #d6d6d6;
    --text-soft: #a8a8a8;
  }
  * { box-sizing: border-box; margin: 0; padding: 0; }
  html, body {
    width: 1200px; height: 720px; overflow: hidden;
    background: var(--backdrop);
    font-family: "Arimo", "Helvetica Neue", Helvetica, Arial, sans-serif;
  }
  .canvas { position: relative; width: 1200px; height: 720px; }
  .card {
    position: absolute; width: 560px; height: 320px; border-radius: 4px;
    background:
      repeating-linear-gradient(90deg, rgba(255,255,255,0.012) 0 1px, transparent 1px 3px),
      radial-gradient(ellipse at 40% 30%, var(--card-sheen) 0%, var(--card-black) 70%);
    box-shadow: 0 6px 18px rgba(0,0,0,0.25);
    color: var(--text-light);
  }
  .card--front { left: 50px; top: 60px; }
  .card--back { left: 590px; top: 340px; }

  .front-brand {
    position: absolute; left: 0; right: 0; top: 100px; text-align: center;
  }
  .brand-name {
    font-size: 44px; font-weight: 700; letter-spacing: 4px; color: var(--metal);
    text-transform: uppercase; line-height: 1;
  }
  .brand-tag {
    margin-top: 8px; font-size: 13px; letter-spacing: 2px; color: var(--metal-dim);
  }
  .front-url {
    position: absolute; left: 0; right: 0; bottom: 48px; text-align: center;
    font-size: 17px; font-weight: 700; letter-spacing: 2px; color: #e8e8e8;
  }

  .back-brand { position: absolute; left: 36px; top: 40px; }
  .back-brand .brand-name { font-size: 34px; letter-spacing: 3px; }
  .back-brand .brand-tag { font-size: 10px; letter-spacing: 1px; margin-top: 5px; }

  .contact-list {
    position: absolute; left: 36px; bottom: 30px; list-style: none;
    font-size: 13px; color: var(--text-light);
  }
  .contact-list li { display: flex; align-items: center; gap: 9px; margin-top: 7px; }
  .contact-list svg { width: 13px; height: 13px; fill: var(--text-soft); flex: none; }

  .person { position: absolute; right: 36px; top: 150px; text-align: right; }
  .person-name { font-size: 17px; font-weight: 700; color: #eaeaea; }
  .person-role { font-size: 13px; color: var(--text-soft); margin-top: 3px; }
</style>
</head>
<body>
<main class="canvas">
  <section class="card card--front" aria-label="Card front">
    <div class="front-brand">
      <div class="brand-name">Orla</div>
      <div class="brand-tag">Property Development</div>
    </div>
    <div class="front-url">www.orla.properties</div>
  </section>

  <section class="card card--back" aria-label="Card back">
    <div class="back-brand">
      <div class="brand-name">Orla</div>
      <div class="brand-tag">Property Development</div>
    </div>

    <div class="person">
      <div class="person-name">Darren Ashcombe</div>
      <div class="person-role">Managing Director</div>
    </div>

    <ul class="contact-list">
      <li><svg viewBox="0 0 16 16"><circle cx="8" cy="8" r="8"/><path d="M5 4l2 2-1 1.2a6 6 0 0 0 2.8 2.8L10 9l2 2-1.2 1.3C7.5 12 4 8.5 3.7 5.2z" fill="#0c0c0c"/></svg>043-861-5207</li>
      <li><svg viewBox="0 0 16 16"><circle cx="8" cy="8" r="8"/><path d="M5 4l2 2-1 1.2a6 6 0 0 0 2.8 2.8L10 9l2 2-1.2 1.3C7.5 12 4 8.5 3.7 5.2z" fill="#0c0c0c"/></svg>1800 417 382 (TF)</li>
      <li><svg viewBox="0 0 16 16"><circle cx="8" cy="8" r="8"/><rect x="3.5" y="5" width="9" height="6" fill="#0c0c0c"/><path d="M3.5 5l4.5 3.5L12.5 5" stroke="#8a8a8a" fill="none"/></svg>darren@orla.properties</li>
      <li><svg viewBox="0 0 16 16"><circle cx="8" cy="8" r="8"/><circle cx="8" cy="8" r="4.5" fill="none" stroke="#0c0c0c"/><path d="M3.5 8h9M8 3.5v9" stroke="#0c0c0c"/></svg>www.orla.properties</li>
      <li><svg viewBox="0 0 16 16"><path d="M8 0a5.5 5.5 0 0 0-5.5 5.5C2.5 10 8 16 8 16s5.5-6 5.5-10.5A5.5 5.5 0 0 0 8 0z"/><circle cx="8" cy="5.5" r="2" fill="#0c0c0c"/></svg>PO BOX 73 ELMVALE, VIC 3024</li>
    </ul>
  </section>
</main>
</body>
</html>
```